Can you create a Business Card based on the Logo you designed.

See example and would like to see other examples.

Trying to keep it very clean with a focus on the logo and name.

```html
<!DOCTYPE html>
<html lang="en">
<head>
<meta charset="utf-8">
<title>Ovrelda Business Card</title>
<link href="https://fonts.googleapis.com/css2?family=Poppins:wght@400;600;700&display=swap" rel="stylesheet">
<style>
  :root {
    --stage: #2b2e31;
    --green-deep: #127a42;
    --green-leaf: #6cbf3f;
    --orange: #f39a2b;
    --paper: #ffffff;
    --ink: #4a4a4a;
    --divider: #f3c99a;
  }
  html, body {
    margin: 0;
    padding: 0;
    width: 1200px;
    height: 900px;
    overflow: hidden;
    background: var(--stage);
    font-family: "Poppins", sans-serif;
  }
  .stage {
    position: relative;
    width: 1200px;
    height: 900px;
  }
  .card {
    position: absolute;
    top: 296px;
    width: 540px;
    height: 309px;
    border-radius: 4px;
    overflow: hidden;
    box-shadow: 0 10px 30px rgba(0,0,0,0.45);
  }
  .card--front { left: 50px; background: var(--paper); }
  .card--back  { left: 610px; background: var(--green-deep); }

  .card__wave { position: absolute; inset: 0; width: 540px; height: 309px; }

  .brand {
    position: absolute;
    display: flex;
    align-items: center;
    gap: 10px;
    font-weight: 700;
    letter-spacing: 0.5px;
  }
  .brand__dot {
    width: 18px;
    height: 18px;
    border-radius: 50%;
    background: var(--orange);
  }
  .card--front .brand {
    left: 0; right: 0; top: 40px;
    justify-content: center;
    font-size: 50px;
    color: var(--green-deep);
  }
  .card--back .brand {
    left: 0; right: 0; top: 0; bottom: 0;
    justify-content: center;
    font-size: 62px;
    color: var(--paper);
  }

  .holder {
    position: absolute;
    left: 40px;
    top: 132px;
  }
  .holder__name {
    margin: 0;
    font-size: 21px;
    font-weight: 700;
    color: var(--green-deep);
    line-height: 1.2;
  }
  .holder__role {
    margin: 2px 0 0;
    font-size: 13px;
    font-weight: 400;
    color: var(--ink);
  }
  .divider {
    position: absolute;
    left: 248px;
    top: 134px;
    width: 1px;
    height: 70px;
    background: var(--divider);
  }
  .contact {
    position: absolute;
    left: 268px;
    top: 132px;
    margin: 0;
    padding: 0;
    list-style: none;
    font-size: 13.5px;
    color: var(--ink);
  }
  .contact__item {
    display: flex;
    align-items: center;
    gap: 8px;
    height: 24px;
  }
  .contact__icon { width: 12px; height: 12px; flex: none; }
</style>
</head>
<body>
<main class="stage">

  <section class="card card--front" aria-label="Business card front">
    <svg class="card__wave" viewBox="0 0 540 309" aria-hidden="true">
      <path d="M0 205 C150 278 330 298 540 303 L540 309 L0 309 Z" fill="var(--green-deep)"/>
      <path d="M0 195 C150 268 330 290 540 295" fill="none" stroke="var(--green-leaf)" stroke-width="2.5"/>
    </svg>

    <div class="brand">
      <span class="brand__name">Ovrelda</span>
      <span class="brand__dot"></span>
    </div>

    <div class="holder">
      <p class="holder__name">Marcus Hale</p>
      <p class="holder__role">Chief Executive Officer</p>
    </div>

    <div class="divider"></div>

    <ul class="contact">
      <li class="contact__item">
        <svg class="contact__icon" viewBox="0 0 12 12" aria-hidden="true"><path d="M2.5 1 L4.5 1 L5.3 3.5 L4 4.4 C4.6 5.8 6.2 7.4 7.6 8 L8.5 6.7 L11 7.5 L11 9.5 C11 10.3 10.3 11 9.5 11 C5 11 1 7 1 2.5 C1 1.7 1.7 1 2.5 1 Z" fill="var(--green-leaf)"/></svg>
        <span>+1 (555) 014-2087</span>
      </li>
      <li class="contact__item">
        <svg class="contact__icon" viewBox="0 0 12 12" aria-hidden="true"><rect x="1" y="2.5" width="10" height="7" rx="1" fill="var(--green-leaf)"/><path d="M1.5 3 L6 6.5 L10.5 3" fill="none" stroke="#fff" stroke-width="1"/></svg>
        <span>ceo@ovrelda-agri.com</span>
      </li>
      <li class="contact__item">
        <svg class="contact__icon" viewBox="0 0 12 12" aria-hidden="true"><circle cx="6" cy="6" r="5" fill="var(--green-leaf)"/><path d="M1 6 H11 M6 1 C3.5 3.5 3.5 8.5 6 11 M6 1 C8.5 3.5 8.5 8.5 6 11" fill="none" stroke="#fff" stroke-width="0.8"/></svg>
        <span>www.ovrelda-agri.com</span>
      </li>
    </ul>
  </section>

  <section class="card card--back" aria-label="Business card back">
    <div class="brand">
      <span class="brand__name">Ovrelda</span>
      <span class="brand__dot"></span>
    </div>
  </section>

</main>
</body>
</html>
```